Maplecrest Insurance Services - Application Designs

My company name is Maplecrest Insurance Services. We are a full service insurance brokerage.

I need an ACH Form (which is attached) to be created with my logo (which is also attached). Please make the ACH Form fillable for info to be entered manually.

In addition I need the Example Quote created with the same color scheme as the Maplecrest Logo. Please create the Example quote as a word document so I can edit the quote and save as a PDF. You can also send me different quote ideas as long as they have the same information on the quote I have attached.

For the Example Supplemental you can leave everything as is and just change the Tillmoor Logo to the attached Maplecrest Insurance Services Logo.

- Change all color-ways to the Maplecrest Insurance Services color-way logo
- Change all the Tillmoor logos to the Maplecrest logo
- Phone number to the company is (555) 317-2096
- Change anything that says Tillmoor to Maplecrest
- Company address is: 7810 Pellway Ave, Unit D Fernbrook CA 90217
- Company Email address is Dana@Maplecrestinsuranceservices.example

Target Market(s)

Clients or Potential Clients

Industry/Entity Type

Insurance

Font styles to use
Serif

Colors
0054AA
0677BA
7BADD7
CADEEF
E8F1F8
00AB8E
00BBA5
67D7C9
C6EFE9
E9F9F6

Requirements
Must have
• Maplecrest Insurance Services Logo

```html
<!DOCTYPE html>
<html lang="en">
<head>
<meta charset="utf-8">
<title>Maplecrest Insurance Services – Workers Compensation Application</title>
<link href="https://fonts.googleapis.com/css2?family=Lato:wght@400;700&family=Montserrat:wght@400&display=swap" rel="stylesheet">
<style>
:root{
  --backdrop:#e6e6e6;
  --paper:#ffffff;
  --navy:#03257a;
  --title-blue:#14549a;
  --row-tint:#e7ecef;
  --rule:#d5dadd;
  --ink:#1d1d1d;
}
*{box-sizing:border-box;margin:0;padding:0}
html,body{width:1200px;height:2400px;overflow:hidden}
body{background:var(--backdrop);font-family:'Lato',sans-serif;color:var(--ink);position:relative}
.page{position:absolute;background:var(--paper)}
.page--one{left:181px;top:124px;width:839px;height:1084px}
.page--two{left:176px;top:1246px;width:848px;height:1098px}
.abs{position:absolute}

.brand{left:17px;top:34px;display:flex;align-items:center;gap:10px}
.brand__mark{width:20px;height:20px;background:var(--navy);flex:none}
.brand__name{font-family:'Lato',sans-serif;font-weight:700;font-size:21px;line-height:1.1;color:var(--navy);white-space:nowrap}
.office{left:637px;top:16px;font-family:'Montserrat',sans-serif;font-size:15px;line-height:17.5px;color:#111;font-style:normal}
.divider{left:0;width:100%;height:1px;background:#e3e3e3}
.form-title{left:0;width:100%;top:118px;text-align:center;font-size:25px;font-weight:400;color:var(--title-blue);letter-spacing:.1px}

.info{left:20px;top:179px;width:802px;height:157px;border:1px solid var(--rule)}
.info__row{position:absolute;left:0;width:100%;display:flex}
.info__row--tint{background:var(--row-tint)}
.cell{font-size:9px;padding:6px 6px;border-right:1px solid var(--rule);height:100%}
.cell:last-child{border-right:none}
.check{font-size:11px;margin-left:12px}

.grid{position:absolute;border-collapse:collapse;table-layout:fixed}
.grid th{background:var(--navy);color:#fff;font-weight:700;font-size:14px;height:29px;border-right:1px solid #fff;text-align:center}
.grid th:last-child{border-right:none}
.grid td{border-right:1px solid var(--rule);border-bottom:1px solid var(--rule);font-size:9px;padding-left:6px}
.grid td:first-child{border-left:1px solid var(--rule)}
.grid tr:nth-child(odd) td{background:var(--row-tint)}
.grid .blank td{background:#fff}

.ops{left:20px;top:520px;width:805px}
.ops__head{background:var(--navy);color:#fff;font-weight:700;font-size:14px;height:28px;line-height:28px;padding-left:6px}
.ops__line{height:28px;border:1px solid var(--rule);border-top:none}

.driving{left:20px;top:702px;width:805px;height:110px;border:1px solid var(--rule);font-size:9px}
.driving__band{position:absolute;left:0;top:50px;width:100%;height:60px;background:var(--row-tint)}
.split{position:absolute;left:404px;top:0;width:1px;height:100%;background:var(--rule)}
.p{position:absolute;white-space:nowrap}

.history{left:19px;top:84px;width:810px}
.history th{text-align:left;padding-left:6px}
.history td{height:28px;vertical-align:top;padding-top:5px}
.history tr:nth-child(even) td{background:#fff}
.history tr:nth-child(odd) td{background:var(--row-tint)}
.small{font-size:9px}
</style>
</head>
<body>

<section class="page page--one">
  <div class="abs brand">
    <span class="brand__mark"></span>
    <span class="brand__name">Maplecrest<br>Insurance Services</span>
  </div>
  <address class="abs office">7810 Pellway Ave, Unit D<br>Fernbrook CA 90217<br>(555) 317-2096</address>
  <div class="abs divider" style="top:105px"></div>
  <h1 class="abs form-title">WORKERS COMPENSATION APPLICATION</h1>
  <div class="abs divider" style="top:161px"></div>

  <div class="abs info">
    <div class="info__row" style="top:0;height:28px">
      <div class="cell" style="width:315px;font-weight:700">Insured</div>
      <div class="cell" style="width:259px;padding-top:8px">Proposed Effective Date</div>
      <div class="cell" style="flex:1">Policy Expiration Date</div>
    </div>
    <div class="info__row info__row--tint" style="top:28px;height:28px;border-top:1px solid var(--rule)">
      <div class="cell" style="width:574px">Contact Person/Title</div>
      <div class="cell" style="flex:1">Federal Tax ID</div>
    </div>
    <div class="info__row" style="top:56px;height:28px;border-top:1px solid var(--rule)">
      <div class="cell" style="width:315px">Telephone Number</div>
      <div class="cell" style="width:259px">Fax Number</div>
      <div class="cell" style="flex:1">E-Mail</div>
    </div>
    <div class="info__row info__row--tint" style="top:84px;height:28px;border-top:1px solid var(--rule)">
      <div class="cell" style="width:315px">Years in Business</div>
      <div class="cell" style="width:259px">No. of Locations</div>
      <div class="cell" style="flex:1">Operations Outside of State? <span class="check">☐Yes ☐No</span></div>
    </div>
    <div class="info__row" style="top:112px;height:44px;border-top:1px solid var(--rule)">
      <div class="cell" style="width:404px">Physical Location</div>
      <div class="cell" style="flex:1">Mailing Location</div>
    </div>
  </div>

  <table class="grid" style="left:20px;top:351px;width:803px">
    <colgroup><col style="width:203px"><col style="width:202px"><col style="width:199px"><col></colgroup>
    <tr><th>Officer Name</th><th>Title</th><th>% of Stock</th><th>Included/Excluded</th></tr>
    <tr class="blank"><td style="height:28px"></td><td></td><td></td><td></td></tr>
    <tr><td style="height:29px"></td><td></td><td></td><td></td></tr>
    <tr class="blank"><td style="height:29px"></td><td></td><td></td><td></td></tr>
    <tr><td style="height:29px"></td><td></td><td></td><td></td></tr>
  </table>

  <div class="abs ops">
    <div class="ops__head">Description of Operations</div>
    <div class="ops__line" style="background:var(--row-tint)"></div>
    <div class="ops__line" style="background:#fff"></div>
    <div class="ops__line" style="background:var(--row-tint)"></div>
    <div class="ops__line" style="background:#fff"></div>
    <div class="ops__line" style="background:var(--row-tint)"></div>
  </div>

  <div class="abs driving">
    <div class="driving__band"></div>
    <div class="split"></div>
    <span class="p" style="left:6px;top:7px">Operation Includes Driving: ☐Yes ☐No</span>
    <span class="p" style="left:6px;top:33px">Driving Radius ☐10-25 mi ☐25-50 mi ☐50-100 mi ☐&gt;100 mi</span>
    <span class="p" style="left:410px;top:4px">Driving Frequency:</span>
    <span class="p" style="left:410px;top:29px">☐ Daily ☐ Weekly ☐ Monthly</span>
    <span class="p" style="left:8px;top:65px">Do you provide group health coverage for your employees: ☐Yes ☐No</span>
    <span class="p" style="left:8px;top:90px">If yes, carrier ____________________________________________________________</span>
    <span class="p" style="left:410px;top:60px">Current Workers Compensation Carrier_______________________________________</span>
    <span class="p" style="left:410px;top:91px">Policy # _________________________________________________________________</span>
  </div>

  <table class="grid" style="left:20px;top:822px;width:803px">
    <colgroup><col style="width:203px"><col style="width:202px"><col style="width:200px"><col></colgroup>
    <tr><th>Class Code</th><th>Payroll</th><th>Number of Full-Time</th><th>Number of Part-Time</th></tr>
    <tr class="blank"><td style="height:28px"></td><td></td><td></td><td></td></tr>
    <tr><td style="height:28px"></td><td></td><td></td><td></td></tr>
    <tr class="blank"><td style="height:30px"></td><td></td><td></td><td></td></tr>
    <tr><td style="height:30px"></td><td></td><td></td><td></td></tr>
    <tr class="blank"><td style="height:30px"></td><td></td><td></td><td></td></tr>
    <tr><td style="height:30px"></td><td></td><td></td><td></td></tr>
  </table>
</section>

<section class="page page--two">
  <span class="abs small" style="left:23px;top:61px">Insured</span>
  <span class="abs small" style="left:598px;top:61px">Policy Renewal Date</span>
  <table class="grid history abs">
    <colgroup><col style="width:165px"><col style="width:325px"><col></colgroup>
    <tr><th></th><th>Payroll Information</th><th>Premium Information</th></tr>
    <tr><td>Current year</td><td></td><td></td></tr>
    <tr><td>Prior year</td><td></td><td></td></tr>
    <tr><td>Prior year</td><td></td><td></td></tr>
    <tr><td>Prior year</td><td></td><td></td></tr>
    <tr><td>Prior year</td><td></td><td></td></tr>
  </table>
</section>

</body>
</html>
```